Slate App design for business management system

TaskOra is a business management system made especially for service based businesses (our subscribers). It enables systemising your service businesses. This can be used by diverse industries like automotive service, beauty (hair salons, nail spas), Spas, Chiropractor, acupuntcure, osteo, yoga studio, business coach, etc.

The UI of the app needs to be designed using flat and clean UI design trends that are currently prevailing for B2C apps. Even the sliding menu panel can be removed and alternative placement of this functionality can be suggested. The color palette used for the design should be limited (3-5 colours)

The Current UI screens are open to suggestions for change. For ease of management in minimum steps, consolidation of functionality on different screens can be suggested, accompanies by a rational reason with the objective of having a simple and straight forward user experience.

User should be able to move from one function to another (booking > view appointments > profile) in no more than 1 or max 2 gestures.

Target Market(s)

SME businesses that provide time based services

Industry/Entity Type

Business

Font styles to use
Sans Serif

Requirements
Must have
• The power point slides give a detailed account of the process flow and functionality that the app is to follow.
• Reference this slide to ensure that your final design must have all screens that are required to deliver the functionality.

```html
<!DOCTYPE html>
<html lang="en">
<head>
<meta charset="utf-8">
<title>TaskOra – Sign In</title>
<link rel="stylesheet" href="https://fonts.googleapis.com/css2?family=Roboto:wght@400;500&family=Great+Vibes&display=swap">
<style>
  :root {
    --status-text: #ffffff;
    --script-brown: #b8690f;
    --field-fill: rgba(255, 255, 255, 0.42);
    --field-edge: rgba(255, 255, 255, 0.75);
    --field-text: #6f6a66;
    --icon-grey: #8f8f8f;
    --action-green: #6db40f;
    --link-text: #fff8ef;
  }
  * { margin: 0; padding: 0; box-sizing: border-box; }
  html, body { width: 1200px; height: 900px; overflow: hidden; }
  body { font-family: "Roboto", Arial, sans-serif; position: relative; }

  .backdrop {
    position: absolute; inset: 0;
    background:
      radial-gradient(ellipse 320px 260px at 5% 100%, rgba(110, 60, 100, 0.85), transparent 70%),
      radial-gradient(ellipse 380px 300px at 18% 62%, rgba(170, 80, 100, 0.7), transparent 70%),
      radial-gradient(ellipse 520px 320px at 40% 78%, rgba(222, 110, 95, 0.85), transparent 70%),
      radial-gradient(ellipse 420px 300px at 95% 72%, rgba(228, 214, 125, 0.95), transparent 70%),
      radial-gradient(ellipse 500px 260px at 70% 55%, rgba(226, 150, 110, 0.7), transparent 70%),
      radial-gradient(ellipse 420px 220px at 35% 30%, rgba(225, 190, 120, 0.8), transparent 70%),
      linear-gradient(180deg, #c8d3b0 0%, #e0d3a0 28%, #e2a27c 58%, #d77366 85%, #cf6a62 100%);
  }

  .status-bar {
    position: absolute; top: 0; left: 0; right: 0; height: 34px;
    display: flex; align-items: center; justify-content: space-between;
    padding: 0 16px 0 18px; color: var(--status-text); font-size: 17px; font-weight: 400;
  }
  .status-left, .status-right { display: flex; align-items: center; gap: 8px; }
  .status-time { position: absolute; left: 50%; transform: translateX(-50%); font-weight: 400; }

  .welcome {
    position: absolute; top: 150px; left: 0; right: 0; text-align: center;
    font-family: "Great Vibes", cursive; font-weight: 400; font-size: 88px;
    color: var(--script-brown); line-height: 1.2;
  }

  .field {
    position: absolute; left: 273px; width: 654px; height: 69px;
    background: var(--field-fill); border: 1px solid var(--field-edge);
    display: flex; align-items: center;
  }
  .field-user { top: 340px; }
  .field-pass { top: 428px; }
  .field-icon { width: 77px; display: flex; justify-content: center; }
  .field-divider { width: 1px; height: 44px; background: rgba(255, 255, 255, 0.8); }
  .field-label { padding-left: 20px; font-size: 18px; font-weight: 400; color: var(--field-text); }

  .login-button {
    position: absolute; left: 273px; top: 577px; width: 654px; height: 68px;
    background: var(--action-green); display: flex; align-items: center; justify-content: center; gap: 16px;
    color: #fff; font-size: 22px; font-weight: 500; letter-spacing: 0.3px;
  }

  .help-links {
    position: absolute; top: 658px; left: 0; right: 0; height: 22px;
    font-size: 16px; color: var(--link-text);
  }
  .help-links a { position: absolute; color: inherit; text-decoration: underline; transform: translateX(-50%); white-space: nowrap; }
  .link-forgot { left: 490px; top: 0; }
  .link-account { left: 705px; top: 2px; }
  .help-divider { position: absolute; left: 600px; top: 0; width: 1px; height: 22px; background: #5a4a40; }
</style>
</head>
<body>
  <div class="backdrop" role="img" aria-label="Softly blurred warm background photo in green, gold, coral and plum tones"></div>

  <header class="status-bar">
    <div class="status-left">
      <span>Slate</span>
      <svg width="18" height="14" viewBox="0 0 18 14" aria-hidden="true">
        <path d="M1 5a11 11 0 0 1 16 0" fill="none" stroke="#fff" stroke-width="2"/>
        <path d="M4 8a7 7 0 0 1 10 0" fill="none" stroke="#fff" stroke-width="2"/>
        <circle cx="9" cy="12" r="1.8" fill="#fff"/>
      </svg>
    </div>
    <span class="status-time">4:21 PM</span>
    <div class="status-right">
      <svg width="10" height="16" viewBox="0 0 10 16" aria-hidden="true">
        <path d="M1 4l8 8-4 3V1l4 3-8 8" fill="none" stroke="rgba(255,255,255,0.8)" stroke-width="1.2"/>
      </svg>
      <span>100%</span>
      <svg width="38" height="16" viewBox="0 0 38 16" aria-hidden="true">
        <rect x="0.5" y="0.5" width="34" height="15" rx="3" fill="none" stroke="#fff"/>
        <rect x="2.5" y="2.5" width="30" height="11" rx="1.5" fill="#fff"/>
        <rect x="35.5" y="5" width="2" height="6" rx="1" fill="#fff"/>
      </svg>
    </div>
  </header>

  <h1 class="welcome">Welcome</h1>

  <div class="field field-user">
    <span class="field-icon">
      <svg width="40" height="40" viewBox="0 0 40 40" aria-hidden="true">
        <circle cx="20" cy="14" r="8.5" fill="none" stroke="var(--icon-grey)" stroke-width="2"/>
        <path d="M3 37c0-9 7-13 17-13s17 4 17 13z" fill="none" stroke="var(--icon-grey)" stroke-width="2" stroke-linejoin="round"/>
      </svg>
    </span>
    <span class="field-divider"></span>
    <span class="field-label">User Name</span>
  </div>

  <div class="field field-pass">
    <span class="field-icon">
      <svg width="30" height="38" viewBox="0 0 30 38" aria-hidden="true">
        <path d="M6 17v-7a9 9 0 0 1 18 0v7" fill="none" stroke="var(--icon-grey)" stroke-width="2"/>
        <rect x="1" y="17" width="28" height="20" rx="2" fill="var(--icon-grey)"/>
      </svg>
    </span>
    <span class="field-divider"></span>
    <span class="field-label">Password</span>
  </div>

  <div class="login-button">
    <svg width="24" height="22" viewBox="0 0 24 22" aria-hidden="true">
      <path d="M7 6V1h16v20H7v-5" fill="none" stroke="#fff" stroke-width="1.6"/>
      <path d="M1 11h13M10 7l4 4-4 4" fill="none" stroke="#fff" stroke-width="1.6"/>
    </svg>
    <span>LOG IN</span>
  </div>

  <nav class="help-links">
    <a class="link-forgot" href="#">Forgot Password?</a>
    <span class="help-divider"></span>
    <a class="link-account" href="#">Need Accound</a>
  </nav>
</body>
</html>
```